Inspiration Poster

Inspirational Poster that has a Dorin Velk like abstract look (http://www.quorvix.com/images/search?q=dorin+velk&FORM=HDRSC2) with the text:

"we walk not in order to arrive at the promise land but because walking itself is a revolution"
-Mark Fennimore

```html
<!DOCTYPE html>
<html lang="en">
<head>
<meta charset="utf-8">
<title>We Walk – Inspirational Poster</title>
<link rel="stylesheet" href="https://fonts.googleapis.com/css2?family=Oswald:wght@500;600&display=swap">
<style>
  :root {
    --paper-light: #e9e1d5;
    --paper-mid: #d6cab8;
    --paper-edge: #b9a891;
    --ink: #4b3526;
    --ink-soft: #8a735f;
    --fist-tone: #c8b6a0;
    --fist-shadow: #a28a72;
  }
  html, body {
    margin: 0;
    padding: 0;
    width: 848px;
    height: 1200px;
    overflow: hidden;
    background: var(--paper-mid);
  }
  .poster {
    position: relative;
    width: 848px;
    height: 1200px;
    overflow: hidden;
    background:
      radial-gradient(ellipse 70% 55% at 50% 42%, var(--paper-light) 0%, var(--paper-mid) 65%, var(--paper-edge) 100%);
  }
  .quote {
    position: absolute;
    inset: 0;
    width: 848px;
    height: 1200px;
    font-family: "Oswald", "Arial Narrow", sans-serif;
    font-weight: 600;
  }
  .quote .line { fill: var(--ink); fill-opacity: 0.92; }
  .quote .line--small { font-weight: 500; }
  .fist-area {
    position: absolute;
    left: 270px;
    top: 730px;
    width: 350px;
    height: 470px;
    border-radius: 48% 48% 20% 20% / 40% 40% 10% 10%;
    background: radial-gradient(ellipse 60% 45% at 50% 35%, var(--fist-tone) 0%, var(--fist-shadow) 55%, rgba(162,138,114,0) 100%);
    opacity: 0.85;
  }
</style>
</head>
<body>
  <div class="poster">
    <div class="fist-area" role="img" aria-label="Faded illustration of a raised clenched fist"></div>
    <svg class="quote" viewBox="0 0 848 1200" xmlns="http://www.w3.org/2000/svg">
      <defs>
        <linearGradient id="revolution-tone" x1="0" y1="0" x2="0" y2="1">
          <stop offset="0" stop-color="var(--ink-soft)"/>
          <stop offset="0.34" stop-color="var(--ink-soft)"/>
          <stop offset="0.34" stop-color="var(--ink)"/>
          <stop offset="1" stop-color="var(--ink)"/>
        </linearGradient>
      </defs>
      <text class="line line--large" x="74" y="326" font-size="138" textLength="680" lengthAdjust="spacingAndGlyphs">WE WALK</text>
      <text class="line line--small" x="74" y="416" font-size="44" textLength="682" lengthAdjust="spacingAndGlyphs">NOT IN ORDER TO ARRIVE AT THE</text>
      <text class="line line--large" x="74" y="528" font-size="108" textLength="680" lengthAdjust="spacingAndGlyphs">PROMISE LAND</text>
      <text class="line line--small" x="74" y="583" font-size="46" textLength="682" lengthAdjust="spacingAndGlyphs">BUT BECAUSE WALKING ITSELF IS A</text>
      <text class="line line--large" x="74" y="708" font-size="135" textLength="682" lengthAdjust="spacingAndGlyphs" style="fill:url(#revolution-tone)">REVOLUTION</text>
    </svg>
  </div>
</body>
</html>
```